Need a book cover design for a Lumora Book on Herbal Remedies

I need a book cover for my new ebook, here are the details:
Title: Meadow Cures
Sub-Heading: Buried Ancient Garden Tonics
Reclaiming the Wisdom of Roots for Everyday Wellness and Strength
Author: Nora Belcourt

```html
<!DOCTYPE html>
<html lang="en">
<head>
<meta charset="utf-8">
<title>Meadow Cures — Book Cover</title>
<link rel="stylesheet" href="https://fonts.googleapis.com/css2?family=Bebas+Neue&family=Oswald:wght@300&family=Poppins:wght@300&display=swap">
<style>
  :root {
    --backdrop: #164404;
    --title-green: #0b6a10;
    --ink: #1e241c;
    --paper: #fbfcf8;
    --mist: #eef3e6;
    --sage: #c9dcb4;
    --leaf: #8fb86a;
    --moss: #6f8f4a;
  }
  * { margin: 0; padding: 0; box-sizing: border-box; }
  html, body {
    width: 1200px;
    height: 1200px;
    overflow: hidden;
    background: var(--backdrop);
  }
  .canvas {
    position: relative;
    width: 1200px;
    height: 1200px;
    background: var(--backdrop);
  }
  .cover {
    position: absolute;
    left: 282px;
    top: 124px;
    width: 636px;
    height: 954px;
    overflow: hidden;
    background: var(--paper);
  }
  .cover-photo {
    position: absolute;
    inset: 0;
    background:
      radial-gradient(ellipse 170px 230px at 560px 740px, #f4f8ec 0%, #dfecc8 55%, rgba(223,236,200,0) 100%),
      radial-gradient(ellipse 150px 160px at 600px 330px, rgba(143,184,106,0.55) 0%, rgba(143,184,106,0) 100%),
      radial-gradient(ellipse 120px 50px at 540px 920px, rgba(111,143,74,0.6) 0%, rgba(111,143,74,0) 100%),
      linear-gradient(180deg, var(--paper) 0%, var(--paper) 35%, var(--mist) 62%, var(--sage) 100%);
  }
  .cover-text {
    position: absolute;
    inset: 0;
    text-align: center;
  }
  .title {
    position: absolute;
    left: 0;
    right: 0;
    top: 128px;
    font-family: "Bebas Neue", sans-serif;
    font-weight: 400;
    font-size: 100px;
    line-height: 90px;
    letter-spacing: 0.09em;
    color: var(--title-green);
    padding-left: 0.09em;
  }
  .subtitle {
    position: absolute;
    left: 0;
    right: 0;
    top: 373px;
    font-family: "Bebas Neue", sans-serif;
    font-size: 30px;
    letter-spacing: 0.04em;
    color: var(--title-green);
  }
  .tagline {
    position: absolute;
    left: 0;
    right: 0;
    top: 518px;
    font-family: "Poppins", sans-serif;
    font-weight: 300;
    font-size: 22px;
    line-height: 42px;
    letter-spacing: 0.05em;
    text-transform: uppercase;
    color: var(--ink);
  }
  .author {
    position: absolute;
    left: 0;
    right: 0;
    top: 746px;
    font-family: "Oswald", sans-serif;
    font-weight: 300;
    font-size: 40px;
    letter-spacing: 0.32em;
    padding-left: 0.32em;
    text-transform: uppercase;
    color: var(--ink);
  }
</style>
</head>
<body>
  <main class="canvas">
    <article class="cover">
      <div class="cover-photo" role="img" aria-label="Soft-focus photo of a white cup of green tea on a saucer, fresh tea leaves and scattered powdered matcha on a pale textured surface"></div>
      <div class="cover-text">
        <h1 class="title">Meadow<br>Cures</h1>
        <p class="subtitle">BURIED ANCIENT GARDEN TONICS</p>
        <p class="tagline">Reclaiming the Wisdom<br>of Roots for Everyday<br>Wellness and Strength</p>
        <p class="author">Nora Belcourt</p>
      </div>
    </article>
  </main>
</body>
</html>
```